Guarenteed! - Homepage Website Design - Coding not required- Winner to complete further pages

Hi all,

We're looking at redesigning our current website with a few adjustments to other pages but the main adjustments will be on the homepage which is what this design request is for. Please note : any of these ideas can be changed if you have something particularly different / special in mind etc.

P.S Coding is not required, just a design.

- Our website -

Our website is simply a price comparison website that allows customers to find companies within their area at the best price. The products available are mostly related to the vehicle trade and all refer to vinyl. This includes the likes of vehicle window tint, vehicle colour change vehicle wrap, vehicle signage as well as other cosmetic vinyl modifications. We allow the customer to search for their product within their chosen area and receive a list of companies who supply their product within that area. From here they can compare prices and view further details on the company.

- What we're looking to do -

We're looking first of all to adjust how the website homepage is displayed, this includes adding images and adjusting the colours that are explained below:

First of all, we look to spread out each of the 12 products (which can be seen on the website as it stands) and add an image to each of the products (all being spaced out as shown in our sketch)

We've been told the website looks too busy so we're thinking if we adjust the colours to more simplier neutral colours as well as the main focus of the website being on the 12 images, that would be great.

- Logo + Banner -

Logo to remain top left although banner may be removed / adjusted to make simplier.

- Colours -

Adjustments - Colours shades
We want the website to still look exciting but simplify the colours. Needs to be kept up to date with the colours / textures etc (bright colours to highlight keypoints)
We're still looking to use either blue or orange or maybe both to highlight these keypoints but the main website to be light colours and maybe even black on white background. The entire homepage can be adjusted colour wise if you feel it fits into your theme including menu bars, banners etc. The key is to get this right with being not too overpowering with the colours but still look interesting and up to date.

- 1 - 4 steps banner - (text may change)

This sits just under the logo and explains to the user how easy the website is to use and the steps they need to take. This may change to a 1 - 5 steps but we're looking to have this designed once the overall colours / theme of the website is sorted.

- 12 images - 4 x 3

This is the main focus of the website and will be the main focus of what the customer sees first of all. This will be where they select their product and then underneath, enter their postcode and distance they would like to search within. As explained further up, we have some of the product images available so if you can where possible add these to the design and then duplicate the images on those we currently don't have available.

- 12 Images -Titles -

These titles will be in this order from left to right and etc

- Colour Change Wrap
- Printed Vehicle Wrap
- Window Tint
- Headlight Tint
- Vehicle Signage
- Shop Signage
- Roof Vinyl Wrap
- Bonnet Vinyl Wrap
- Carbon Fibre Vinyl
- Stickerbomb Vinyl
- Clear Protective Vinyl
- Wheel Refurb

Text to be quite large, centered and with the o to the left of the title. Short titles like 'Window Tint' should fit on one line in the middle of the box where as titles such as ' Stickerbomb Vinyl Wrap' should have the 'Stickerbomb Vinyl' on the first line with the 'Wrap' on the line below. The background of this text is up to experient, might be worth just a simple colour or it might be worth using a bright blue or orange to keep in with the theme of the logo etc.

These will also have the circle tick box to the left of the title (as on the current website) where the customer clicks to select the product they have available.
We were also thinking that if when the customer ticks the circle on their selected box, the box is highlighted in some way to show this.

- Search Block -

This will appear under the 12 images and allows the customer to input their postcode and distance for the search criteria. Colours on this can of course be adjusted to keep in theme with the website.

- Under the 12 Images -

- Block underneath the 12 images and search block -

To the left will be some key bullet points about the website - maybe 4 or 5 with a green tick to the left of this. Background colour will probably be best to be a light colour, possibly grey.

Then to the right of this will appear 4 images, 2 before and 2 after when applying these products. Images to be used aren't fully decided on and we would like this stage of the design left to the end when the rest of the theme etc have been decided on.

Attached images are as follows :
- How the website looks as it stands
- The fold line on the website (obviously important)
- Our rough sketch of how we'd like the website homepage to look.
- We have 7 of the images ready that are all attached in this one file. Please duplicate the images on those that currently don't have the image available.

We will also be requesting a website developer to put this into action if our current designer falls through so please feel free to contact us if potentially interested.

The layout can change if you can think of something particular different / unique that works with this design. The main idea is to not only get the 12 products on view to the viewers but also the keypoints and before and after images.

Any questions, please ask away as we're bound to have forgotten a few things.

Thanks and good luck!

Hi all, keep the designs coming.

We haven't quite seen that extra special design we're after. As stated, we're after something fairly simple to suit the youth as well as the middle aged but we're also after something that bit special.

Colours to concentrate on are still and orange etc although feel free to use other colours if you have anything special in mind.

Please experience and we'll give you our honest feedback.

Many thanks all and good luck!

Hi all, this is a message to all the designers.

Some good designs coming in but we're still after that something special for the website design. Keep the designs coming and please feel free to experiment with the design colours, layout etc.

The basic principle of the website needs to remain regarding the 12 products, search within block and 4 steps all appearing on the homepage.

The 4 steps seems to work best when it's got text as well as some simple images next to this.

A variation with the product titles with how to display this, some designers have gone with a simple white background whereas others have gone with colours. Please experiment here and where possible, add a contract / texture to the colour. Please remember the product titles needs to be clear, centured and with the circle tick box to the left of it. 

We're after a fairly simple design although we need it to look 21st century, up to date as well as interesting. The key points straight away are the 4 steps as well as the 12 products so try to guide the viewer to these areas a little.

White background behind the 12 images seems to be a much, although a light colour could possibly work.

The keypoints underneath these 12 products are too very important as it outlines what we do etc. Tick colour can vary.

Next to these keypoints will be the 'before' and 'after' images, these images needs to be fairly small and ensure there is white background around the image itself.

Good luck all and any questions, feel free to ask away.

Thanks!

Hi,

 Thank you for your time and effort with these designs, we are very nearly there with the design but we've thought of something that may work for the homepage. A curved arrow from step 1 pointing to the products, this may or may not work but feel free to give it a go.

Many thanks,

Thank you to everyone for your time and efforts with the design. It's hugely appreciated so thank you all once again.

Wish you all the luck in the future.

```html
<!DOCTYPE html>
<html lang="en">
<head>
<meta charset="utf-8">
<title>WrapScout – Find and Compare Vinyl Installers</title>
<link href="https://fonts.googleapis.com/css2?family=Roboto+Condensed:wght@400;700&family=Source+Sans+3:wght@300;400;600;700&family=Kalam:wght@400&display=swap" rel="stylesheet">
<style>
:root{
  --navy:#2c4a86;
  --navy-dark:#1f3768;
  --orange:#e5692b;
  --orange-light:#f08a2e;
  --text-blue:#2a3f73;
  --grey-bg:#e4e4e4;
  --grey-card:#e9e9e9;
  --panel-pale:#f7e7df;
  --footer:#333333;
  --white:#ffffff;
  --ink:#333333;
}
*{box-sizing:border-box;margin:0;padding:0}
html,body{width:1200px;height:2179px;overflow:hidden}
body{position:relative;background:var(--white);font-family:"Source Sans 3",Arial,sans-serif;color:var(--ink)}
.abs{position:absolute}

/* header */
.site-header{left:0;top:0;width:1200px;height:127px;background:linear-gradient(#ffffff,#ececec)}
.brand{left:145px;top:30px;display:flex;align-items:center;gap:14px;font-family:"Roboto Condensed",sans-serif;font-weight:700;font-size:50px;color:var(--navy);letter-spacing:1px}
.brand-dot{width:48px;height:48px;border-radius:50%;background:var(--orange)}
.brand-tag{left:145px;top:92px;font-size:17px;font-weight:600;color:var(--navy);letter-spacing:.5px}
.promo{left:505px;top:5px;width:553px;height:115px;background:linear-gradient(#f7a13a,#e6762a);border-radius:4px;overflow:hidden}
.promo-title{left:0;top:0;width:553px;height:40px;background:var(--navy);color:#fff;font-family:"Roboto Condensed",sans-serif;font-weight:700;font-size:23px;text-align:center;line-height:40px;letter-spacing:.5px}
.promo-line{left:16px;top:58px;color:#fff;font-size:24px;font-weight:600}
.promo-line b{font-size:34px}
.promo-map{left:345px;top:44px;width:200px;height:66px;background:linear-gradient(120deg,#e9eee3,#c9d9c1);border-radius:3px}

/* nav */
.main-nav{left:0;top:127px;width:1200px;height:42px;background:linear-gradient(var(--navy),var(--navy-dark));display:flex;padding-left:124px}
.main-nav a{color:#fff;text-decoration:none;font-family:"Roboto Condensed",sans-serif;font-weight:700;font-size:18px;line-height:42px;padding:0 18px;border-right:1px solid rgba(255,255,255,.18)}
.main-nav a:last-of-type{border-right:none}
.social{top:132px;width:34px;height:34px;background:#4a6fb0;border:1px solid rgba(255,255,255,.35)}

/* how it works */
.steps{left:0;top:169px;width:1200px;height:316px;background:radial-gradient(ellipse at 50% 40%,#f4f4f4,#d5d5d5)}
.steps-title{left:0;top:18px;width:1200px;text-align:center;font-family:"Kalam",cursive;font-size:40px;font-weight:400;color:#444}
.step{top:70px;width:234px;height:246px;text-align:center}
.step+.step{border-left:1px solid rgba(255,255,255,.7)}
.step-num{margin:14px auto 0;width:40px;height:40px;border-radius:50%;background:radial-gradient(circle at 40% 35%,var(--orange-light),var(--orange));color:#fff;font-weight:700;font-size:20px;line-height:40px;box-shadow:0 2px 3px rgba(0,0,0,.25)}
.step-icon{margin:22px auto 0;height:64px;display:flex;align-items:center;justify-content:center}
.step-label{margin-top:14px;font-size:16px;line-height:19px;color:var(--text-blue)}
.steps-shadow{left:140px;top:485px;width:920px;height:10px;background:radial-gradient(ellipse at 50% 0,rgba(0,0,0,.2),transparent 70%)}

/* products */
.product{width:216px;height:225px;border:1px solid #d8d8d8;background:#fff}
.product-photo{position:absolute;left:8px;top:8px;width:198px;height:158px}
.product-label{position:absolute;left:0;bottom:0;width:214px;height:51px;background:linear-gradient(#f2f2f2,#dcdcdc);display:flex;align-items:center;justify-content:center;text-align:center;font-family:"Roboto Condensed",sans-serif;font-size:15px;line-height:16px;color:var(--text-blue);text-transform:uppercase}
.tick{position:absolute;right:10px;top:8px;width:30px;height:30px;border-radius:50%;background:#e6e6e6;border:1px solid #c9c9c9;display:flex;align-items:center;justify-content:center}
.tick.is-selected{background:var(--orange);border-color:var(--orange)}
.product.is-selected{border-color:var(--orange)}

/* search */
.search-band{left:0;top:1303px;width:1200px;height:191px;background:repeating-linear-gradient(45deg,#ededed 0 2px,#f8f8f8 2px 5px)}
.search-bar{left:142px;top:36px;width:916px;height:75px;background:var(--navy);border-radius:6px;box-shadow:0 3px 6px rgba(0,0,0,.2)}
.search-title{left:14px;top:0;width:262px;line-height:75px;color:#fff;font-family:"Roboto Condensed",sans-serif;font-weight:400;font-size:32px;letter-spacing:2px;white-space:nowrap}
.search-title b{font-weight:700}
.field{top:19px;height:42px;background:#fff;border-radius:3px;font-size:15px;line-height:42px;padding:0 14px;color:#444}
.field span{position:absolute;right:10px;color:#bbb;font-size:13px}
.search-of{left:520px;top:0;line-height:75px;color:#fff;font-size:24px;font-weight:700}
.search-btn{left:793px;top:19px;width:109px;height:42px;background:var(--orange);border-radius:3px;color:#fff;font-family:"Roboto Condensed",sans-serif;font-weight:700;font-size:18px;display:flex;align-items:center;justify-content:center;gap:6px}

/* features */
.features{left:0;top:1494px;width:1200px;height:434px;background:var(--orange)}
.keypoints{left:183px;top:1479px;width:367px;height:467px;background:var(--panel-pale);box-shadow:0 2px 6px rgba(0,0,0,.25);padding:26px 22px 0 24px}
.keypoints h2{font-weight:300;font-size:30px;color:#333;padding-bottom:10px;border-bottom:1px solid #d7c4b9}
.keypoints ul{list-style:none;margin-top:24px}
.keypoints li{position:relative;padding-left:28px;font-size:16px;line-height:22px;color:#444;margin-bottom:26px}
.keypoints li svg{position:absolute;left:2px;top:4px}
.ba-head{top:1505px;width:225px;color:#fff;font-weight:300;font-size:27px;padding-bottom:8px;border-bottom:1px solid rgba(255,255,255,.5)}
.ba-frame{width:225px;height:149px;background:#fff;box-shadow:0 2px 5px rgba(0,0,0,.25);padding:12px}
.ba-frame div{width:100%;height:100%}

/* footer */
.site-footer{left:0;top:1969px;width:1200px;height:210px;background:var(--footer)}
.footer-zig{left:0;top:1959px}
.footer-title{left:0;top:2006px;width:1200px;text-align:center;color:#fff;font-weight:300;font-size:33px}
.mail-field{top:2065px;height:44px;background:#fff;font-size:15px;line-height:44px;padding-left:14px;color:#999}
.mail-submit{left:780px;top:2065px;width:93px;height:44px;background:#e5501d;color:#fff;font-family:"Roboto Condensed",sans-serif;font-weight:700;font-size:18px;line-height:44px;text-align:center}
.copyright{left:0;top:2141px;width:1200px;text-align:center;color:#ccc;font-size:12px}
</style>
</head>
<body>

<header class="abs site-header">
  <div class="abs brand"><span class="brand-dot"></span>WrapScout</div>
  <div class="abs brand-tag">Find and Compare Vinyl Installers</div>
  <div class="abs promo">
    <div class="abs promo-title">FIND A PROFESSIONAL VINYL INSTALLER TODAY</div>
    <div class="abs promo-line">Search Save in <b>Seconds!</b></div>
    <div class="abs promo-map" role="img" aria-label="Map of nearby towns with a location marker"></div>
  </div>
</header>

<nav class="abs main-nav">
  <a>HOME</a><a>ABOUT US</a><a>CONTACT US</a><a>BLOG</a><a>LIST YOUR COMPANY HERE</a>
</nav>
<div class="abs social" style="left:986px" aria-label="Social link"></div>
<div class="abs social" style="left:1024px;background:#4aa3d8" aria-label="Social link"></div>

<section class="abs steps">
  <h1 class="abs steps-title">How it works</h1>
  <div class="abs step" style="left:132px">
    <div class="step-num">1</div>
    <div class="step-icon"><svg width="84" height="36" viewBox="0 0 84 36"><path d="M4 26 C4 18 14 16 22 15 L32 6 C38 2 54 2 60 8 L68 15 C76 16 82 19 82 25 L82 28 L4 28 Z" fill="var(--text-blue)"/><circle cx="20" cy="28" r="7" fill="var(--text-blue)"/><circle cx="66" cy="28" r="7" fill="var(--text-blue)"/></svg></div>
    <div class="step-label">Select Chosen<br>Product</div>
  </div>
  <div class="abs step" style="left:366px">
    <div class="step-num">2</div>
    <div class="step-icon"><svg width="50" height="62" viewBox="0 0 50 62"><path d="M25 2 C12 2 4 11 4 22 C4 36 25 58 25 58 C25 58 46 36 46 22 C46 11 38 2 25 2 Z" fill="var(--text-blue)"/><circle cx="25" cy="21" r="8" fill="#e2e2e2"/></svg></div>
    <div class="step-label">Input Postcode,<br>Distance &amp; Search</div>
  </div>
  <div class="abs step" style="left:600px">
    <div class="step-num">3</div>
    <div class="step-icon"><svg width="60" height="60" viewBox="0 0 60 60"><path d="M30 4 L56 4 L56 30 L28 58 L2 32 Z" fill="var(--text-blue)"/><circle cx="45" cy="15" r="5" fill="#e2e2e2"/><text x="24" y="38" fill="#e2e2e2" font-size="16" font-weight="700" font-family="Source Sans 3, sans-serif" transform="rotate(-45 24 34)">£</text></svg></div>
    <div class="step-label">Compare<br>Companies &amp; Prices</div>
  </div>
  <div class="abs step" style="left:834px">
    <div class="step-num">4</div>
    <div class="step-icon"><svg width="62" height="54" viewBox="0 0 62 54"><path d="M4 18 C4 6 58 6 58 18 L58 22 L46 22 L44 15 L18 15 L16 22 L4 22 Z" fill="var(--text-blue)"/><path d="M14 26 L48 26 L54 50 L8 50 Z" fill="var(--text-blue)"/><circle cx="31" cy="38" r="7" fill="#e2e2e2"/></svg></div>
    <div class="step-label">Contact Chosen<br>Company</div>
  </div>
</section>
<div class="abs steps-shadow"></div>

<div class="abs product" style="left:142px;top:528px"><div class="product-photo" role="img" aria-label="Red SUV with a colour change wrap" style="background:linear-gradient(160deg,#fff 20%,#e23b2e 50%,#8a1e18 75%,#fff 90%)"></div><span class="tick"><svg width="14" height="12"><path d="M2 6 L6 10 L12 2" stroke="#777" stroke-width="2" fill="none"/></svg></span><div class="product-label">Colour Change<br>Wrap</div></div>
<div class="abs product" style="left:376px;top:528px"><div class="product-photo" role="img" aria-label="Van with a full printed wrap" style="background:linear-gradient(170deg,#fff 15%,#9cc4e6 35%,#5d9c3e 60%,#fff 85%)"></div><span class="tick"><svg width="14" height="12"><path d="M2 6 L6 10 L12 2" stroke="#777" stroke-width="2" fill="none"/></svg></span><div class="product-label">Printed Vehicle<br>Wrap</div></div>
<div class="abs product is-selected" style="left:610px;top:528px"><div class="product-photo" role="img" aria-label="Green hatchbacks with tinted windows" style="background:linear-gradient(160deg,#fff 10%,#4fb548 40%,#2e7d2a 60%,#fff 90%)"></div><span class="tick is-selected"><svg width="14" height="12"><path d="M2 6 L6 10 L12 2" stroke="#fff" stroke-width="2" fill="none"/></svg></span><div class="product-label">Window Tint</div></div>
<div class="abs product" style="left:844px;top:528px"><div class="product-photo" role="img" aria-label="Silver coupe front with tinted headlights" style="background:linear-gradient(170deg,#fff 15%,#cfd6dc 40%,#8c96a0 65%,#fff 90%)"></div><span class="tick"><svg width="14" height="12"><path d="M2 6 L6 10 L12 2" stroke="#777" stroke-width="2" fill="none"/></svg></span><div class="product-label">Headlight Tint</div></div>

<div class="abs product" style="left:142px;top:791px"><div class="product-photo" role="img" aria-label="White van with company signage" style="background:linear-gradient(170deg,#fff 20%,#ececec 45%,#b5b5b5 65%,#fff 90%)"></div><span class="tick"><svg width="14" height="12"><path d="M2 6 L6 10 L12 2" stroke="#777" stroke-width="2" fill="none"/></svg></span><div class="product-label">Vehicle Signage</div></div>
<div class="abs product" style="left:376px;top:791px"><div class="product-photo" role="img" aria-label="Shop front with window signage" style="background:linear-gradient(#bfc3c7 0 18%,#2b2b2b 18% 75%,#9a9a9a 75%)"></div><span class="tick"><svg width="14" height="12"><path d="M2 6 L6 10 L12 2" stroke="#777" stroke-width="2" fill="none"/></svg></span><div class="product-label">Shop Signage</div></div>
<div class="abs product" style="left:610px;top:791px"><div class="product-photo" role="img" aria-label="Silver car from above with a black roof wrap" style="background:linear-gradient(135deg,#fff 15%,#c7c9cc 40%,#3a3a3a 55%,#a9acb0 70%,#fff 90%)"></div><span class="tick"><svg width="14" height="12"><path d="M2 6 L6 10 L12 2" stroke="#777" stroke-width="2" fill="none"/></svg></span><div class="product-label">Roof Vinyl<br>Wrap</div></div>
<div class="abs product" style="left:844px;top:791px"><div class="product-photo" role="img" aria-label="Silver car from above with a black bonnet wrap" style="background:linear-gradient(135deg,#fff 15%,#3a3a3a 35%,#c7c9cc 55%,#a9acb0 70%,#fff 90%)"></div><span class="tick"><svg width="14" height="12"><path d="M2 6 L6 10 L12 2" stroke="#777" stroke-width="2" fill="none"/></svg></span><div class="product-label">Bonnet Vinyl<br>Wrap</div></div>

<div class="abs product" style="left:142px;top:1056px"><div class="product-photo" role="img" aria-label="Car interior trim in carbon fibre vinyl" style="background:linear-gradient(150deg,#2a2f36,#0f1114 60%,#53585e)"></div><span class="tick"><svg width="14" height="12"><path d="M2 6 L6 10 L12 2" stroke="#777" stroke-width="2" fill="none"/></svg></span><div class="product-label">Carbon Fibre<br>Vinyl</div></div>
<div class="abs product" style="left:376px;top:1056px"><div class="product-photo" role="img" aria-label="White car with a stickerbombed bonnet" style="background:linear-gradient(170deg,#fff 10%,#e9b23a 30%,#d3452f 45%,#3b7fc4 55%,#e6e6e6 70%,#fff 90%)"></div><span class="tick"><svg width="14" height="12"><path d="M2 6 L6 10 L12 2" stroke="#777" stroke-width="2" fill="none"/></svg></span><div class="product-label">Stickerbomb<br>Vinyl</div></div>
<div class="abs product" style="left:610px;top:1056px"><div class="product-photo" role="img" aria-label="Clear protective film being applied to paintwork" style="background:linear-gradient(140deg,#2b2d5c,#6b6fa8 45%,#c9cbe0 65%,#3a3c6e)"></div><span class="tick"><svg width="14" height="12"><path d="M2 6 L6 10 L12 2" stroke="#777" stroke-width="2" fill="none"/></svg></span><div class="product-label">Clear Protective<br>Vinyl</div></div>
<div class="abs product" style="left:844px;top:1056px"><div class="product-photo" role="img" aria-label="Refurbished alloy wheel" style="background:radial-gradient(circle,#e6e8ea 20%,#9aa0a6 45%,#2c2c2c 60%,#4a3d30 85%)"></div><span class="tick"><svg width="14" height="12"><path d="M2 6 L6 10 L12 2" stroke="#777" stroke-width="2" fill="none"/></svg></span><div class="product-label">Wheel Refurb</div></div>

<section class="abs search-band">
  <div class="abs search-bar">
    <div class="abs search-title"><b>SEARCH</b> WITHIN</div>
    <div class="abs field" style="left:285px;width:216px">10<span>MILES</span></div>
    <div class="abs search-of">of</div>
    <div class="abs field" style="left:557px;width:218px">90210<span>ZIP</span></div>
    <div class="abs search-btn">SEARCH <svg width="16" height="16"><circle cx="6.5" cy="6.5" r="4.5" stroke="#fff" stroke-width="2" fill="none"/><path d="M10 10 L14 14" stroke="#fff" stroke-width="2.5"/></svg></div>
  </div>
</section>

<section class="abs features"></section>
<div class="abs keypoints">
  <h2>Lorem Ipsum</h2>
  <ul>
    <li><svg width="14" height="12"><path d="M1 6 L5 10 L13 1" stroke="var(--orange)" stroke-width="2" fill="none"/></svg>Lorem ipsum dolor sit amet, consectetur adipiscing elit.</li>
    <li><svg width="14" height="12"><path d="M1 6 L5 10 L13 1" stroke="var(--orange)" stroke-width="2" fill="none"/></svg>Nulla non libero interdum, bibendum est ut, pulvinar mi.</li>
    <li><svg width="14" height="12"><path d="M1 6 L5 10 L13 1" stroke="var(--orange)" stroke-width="2" fill="none"/></svg>Nulla sit amet mi sed magna eleifend auctor nec non turpis.</li>
    <li><svg width="14" height="12"><path d="M1 6 L5 10 L13 1" stroke="var(--orange)" stroke-width="2" fill="none"/></svg>Nullam vel tortor blandit, ultricies dui vitae, congue lacus.</li>
    <li><svg width="14" height="12"><path d="M1 6 L5 10 L13 1" stroke="var(--orange)" stroke-width="2" fill="none"/></svg>Aenean tincidunt ipsum consequat arcu interdum tempor.</li>
  </ul>
</div>
<div class="abs ba-head" style="left:599px">Before</div>
<div class="abs ba-head" style="left:844px">After</div>
<div class="abs ba-frame" style="left:599px;top:1575px"><div role="img" aria-label="Plain white van before signage" style="background:radial-gradient(ellipse,#dcdcdc 30%,#fff 70%)"></div></div>
<div class="abs ba-frame" style="left:844px;top:1575px"><div role="img" aria-label="White van after signage is applied" style="background:radial-gradient(ellipse,#c9c9c9 30%,#fff 70%)"></div></div>
<div class="abs ba-frame" style="left:599px;top:1742px"><div role="img" aria-label="Green hatchback before window tint" style="background:radial-gradient(ellipse,#4fb548 25%,#fff 65%)"></div></div>
<div class="abs ba-frame" style="left:844px;top:1742px"><div role="img" aria-label="Green hatchback after window tint" style="background:radial-gradient(ellipse,#2e7d2a 25%,#fff 65%)"></div></div>

<svg class="abs footer-zig" width="1200" height="12" viewBox="0 0 1200 12"><path d="M0 12 L0 10 L10 2 L20 10 L30 2 L40 10 L50 2 L60 10 L70 2 L80 10 L90 2 L100 10 L110 2 L120 10 L130 2 L140 10 L150 2 L160 10 L170 2 L180 10 L190 2 L200 10 L210 2 L220 10 L230 2 L240 10 L250 2 L260 10 L270 2 L280 10 L290 2 L300 10 L310 2 L320 10 L330 2 L340 10 L350 2 L360 10 L370 2 L380 10 L390 2 L400 10 L410 2 L420 10 L430 2 L440 10 L450 2 L460 10 L470 2 L480 10 L490 2 L500 10 L510 2 L520 10 L530 2 L540 10 L550 2 L560 10 L570 2 L580 10 L590 2 L600 10 L610 2 L620 10 L630 2 L640 10 L650 2 L660 10 L670 2 L680 10 L690 2 L700 10 L710 2 L720 10 L730 2 L740 10 L750 2 L760 10 L770 2 L780 10 L790 2 L800 10 L810 2 L820 10 L830 2 L840 10 L850 2 L860 10 L870 2 L880 10 L890 2 L900 10 L910 2 L920 10 L930 2 L940 10 L950 2 L960 10 L970 2 L980 10 L990 2 L1000 10 L1010 2 L1020 10 L1030 2 L1040 10 L1050 2 L1060 10 L1070 2 L1080 10 L1090 2 L1100 10 L1110 2 L1120 10 L1130 2 L1140 10 L1150 2 L1160 10 L1170 2 L1180 10 L1190 2 L1200 10 L1200 12 Z" fill="var(--footer)"/></svg>
<footer class="abs site-footer"></footer>
<div class="abs footer-title">Join Our Mailing List</div>
<div class="abs mail-field" style="left:327px;width:216px">Your name...</div>
<div class="abs mail-field" style="left:553px;width:217px">Your email...</div>
<div class="abs mail-submit">SUBMIT</div>
<div class="abs copyright">Copyright © 2013 WrapScout.</div>

</body>
</html>
```